2020 Lone Ridge Crisis Alliance Conference Event flyer for annual conference held in Amarillo Texas

The Power of Connection

I need a flyer to send out via email. I The flyer will depict our theme, "The Power of Connection" event dates, website and costs. Association is Lone Ridge Crisis Alliance, date April 23-25, 2020, website www.loneridgealliance.org, Early Bird and Member discounts location Harborview Lodge, Amarillo Texas

page 2 will have sponsor info, and keynote description, can be 3 pages if absolutely necessary
: keynote speaker Martin Oakley, Martin is a retired Westbrook Roadway Patrol officer who spent more than 17 years patrolling the Silverfall Span Bridge. During that time he encountered hundreds of people who were troubled and had lost hope. They were ready to jump off the bridge and end their lives. Although a trained negotiator, Oakley also relied on his compassion, gentle voice, eye contact, and his innate ability to “listening to understand”. During his career, he encouraged more than 200 people not to jump, go over the bridge’s rail or come back to solid ground from where they had been standing precariously. These challenging, but rewarding efforts earned him the nickname, “Guardian of the Silverfall Span Bridge”. Retired, Oakley is now dedicating his life to promoting mental health awareness and suicide prevention across the globe.
Great sponsor opportunities available at www.Loneridgealliance.org sponsor letter attached for info on sponsor opportunities it is not necessary to include all info

i attached a mockup page 1 flyer that i really like but graphic designer did not complete this would give you an idea of what i am looking for on page 1 although it is missing a few elements

the Brookhaven (logo attached) is a champion sponsor, Plainsview Visitors Bureau (logo attached)

Target Market(s)

law enforcement, hospitals, mental health providers, court system,

Colors

Designer to choose colors to be used in the design.

Requirements
Must have
• theme -The Power of Connection
• website
• dates
• location
• costs
Nice to have
• prefer graphic related to theme
• Brookhaven is a large sponsor
• need to have 2-3 pages for all info
• include info on sponsor opportunities but does not have to include all info on attachment

```html
<!DOCTYPE html>
<html lang="en">
<head>
<meta charset="utf-8">
<title>The Power of Connection 2020 – Lone Ridge Crisis Alliance</title>
<link href="https://fonts.googleapis.com/css2?family=Montserrat:wght@300;400;500;600;700;800&family=Great+Vibes&family=Archivo+Black&display=swap" rel="stylesheet">
<style>
:root{
  --navy:#4b5677;
  --slate:#4f5670;
  --panel:#4a4a4a;
  --ink:#3c3c3c;
  --mist:#e8e9eb;
  --blush:#e6d6d7;
  --green:#2f6a3a;
  --red:#e8232d;
  --gold:#c9963a;
  --white:#ffffff;
}
*{margin:0;padding:0;box-sizing:border-box}
html,body{width:849px;height:1200px;overflow:hidden}
body{font-family:"Montserrat",sans-serif;color:var(--ink);background:var(--white)}
.flyer{position:relative;width:849px;height:1200px;overflow:hidden;
  background:linear-gradient(160deg,#f1eeef 0%,var(--blush) 100%)}
.backdrop{position:absolute;inset:0}
.topline{position:absolute;top:32px;left:0;width:849px;text-align:center;font-weight:700;font-size:16.5px;color:#3e3e3e;letter-spacing:.2px}
.photo{position:absolute;left:22px;top:160px;width:300px;height:286px;border-radius:16px;
  background:linear-gradient(160deg,#6b6f7a 0%,#3b3e47 55%,#2b2d33 100%)}
.about{position:absolute;left:22px;top:452px;width:302px;color:var(--white)}
.about h2{font-weight:400;font-size:21px;margin-bottom:12px}
.about h2 b{font-weight:700}
.about p{font-size:12.9px;line-height:16.9px;text-align:justify;font-weight:300;letter-spacing:.15px}
.pointer{position:absolute;left:132px;top:847px}
.agenda{position:absolute;left:29px;top:860px;width:310px;color:var(--white)}
.agenda h3{font-family:"Archivo Black",sans-serif;font-size:23px;margin-bottom:12px;letter-spacing:.3px}
.agenda li{list-style:none;font-size:9.4px;font-weight:700;line-height:10.4px;margin-bottom:12px}
.agenda .time{font-family:"Archivo Black",sans-serif;font-weight:400;display:block}
.badge{position:absolute;left:444px;top:118px;width:176px;height:176px;border-radius:50%;
  background:#e3e3e6;display:flex;align-items:center;justify-content:center}
.badge-ring{width:142px;height:142px;border-radius:50%;background:var(--white);border:5px solid #b9bbc2;
  display:flex;align-items:center;justify-content:center}
.badge-mark{width:112px;height:112px;border-radius:50%;border:6px solid #2d4d9c;
  display:flex;align-items:center;justify-content:center;text-align:center;
  font-weight:700;font-size:11px;line-height:13px;color:#2d4d9c;padding:8px}
.kicker{position:absolute;left:440px;top:292px;width:390px;text-align:center;font-weight:700;font-size:15px;color:var(--slate)}
.title-main{position:absolute;left:440px;top:305px;width:380px;text-align:right;font-weight:700;font-size:66px;letter-spacing:-2.5px;color:var(--slate)}
.title-script{position:absolute;left:360px;top:378px;width:470px;text-align:right;font-family:"Great Vibes",cursive;font-size:82px;line-height:90px;color:var(--slate)}
.title-script small{font-size:30px;vertical-align:28px;margin-right:2px}
.title-year{position:absolute;left:560px;top:455px;width:240px;text-align:right;font-weight:700;font-size:54px;color:var(--ink)}
.welcome{position:absolute;left:362px;top:528px;width:462px}
.welcome h2{text-align:center;font-weight:700;font-size:24px;color:#515151;margin-bottom:10px}
.welcome p{font-size:13.6px;line-height:17.4px;text-align:justify;color:#333}
.registration{position:absolute;left:362px;top:742px;width:462px;height:194px;border:1.5px dashed var(--gold);padding:18px 12px 0 10px}
.registration h3{font-family:"Archivo Black",sans-serif;font-weight:400;font-size:17px;color:#303030;margin-bottom:8px}
.price{font-size:23.5px;font-weight:500;color:#333;line-height:29px}
.registration p{font-size:9.6px;line-height:13px;margin-top:8px;color:#333}
.discounts{position:absolute;left:366px;top:947px;font-weight:700;font-size:22.8px;color:var(--green)}
.contact{position:absolute;left:378px;top:994px;font-weight:700;color:#3a3a3a}
.contact .q{font-size:17px;margin-bottom:8px}
.contact .mail{font-size:18px;display:flex;align-items:center;gap:8px}
.sponsors{position:absolute;left:373px;top:1066px;width:450px}
.sponsors .label{font-size:12px;color:#333;margin-bottom:8px}
.sponsor-row{display:flex;align-items:center;justify-content:space-between;padding-right:24px}
.sponsor-name{font-size:16px;font-weight:700;color:var(--ink)}
.footer{position:absolute;left:0;top:1133px;width:849px;height:67px;background:var(--red);
  display:flex;align-items:center;justify-content:space-between;padding:0 20px;color:var(--white);white-space:nowrap}
.footer span{font-size:18.5px;font-weight:400}
.footer strong{font-size:27px;font-weight:400}
</style>
</head>
<body>
<main class="flyer">
  <svg class="backdrop" width="849" height="1200" viewBox="0 0 849 1200" aria-hidden="true">
    <path d="M0 20 C80 40 230 90 346 140 V1133 H0 Z" fill="#4a4a4a"/>
    <path d="M0 0 H849 V20 C760 80 660 150 540 170 C470 180 400 165 346 140 C230 90 80 40 0 20 Z" fill="#e8e9eb"/>
    <path d="M0 0 H210 C140 10 60 30 0 60 Z" fill="#4b5677"/>
    <path d="M849 18 C780 90 690 150 580 178 L575 172 C690 140 780 70 849 0 Z" fill="#4b5677"/>
  </svg>

  <div class="topline">2020 LONE RIDGE CRISIS ALLIANCE ANNUAL CONFERENCE</div>

  <div class="photo" role="img" aria-label="Portrait photo of keynote speaker Martin Oakley speaking on stage"></div>

  <section class="about">
    <h2>About <b>Martin Oakley</b></h2>
    <p>Martin is a retired Westbrook Roadway Patrol officer who spent more than 17 years patrolling the Silverfall Span Bridge. During that time he encountered hundreds of people who were troubled and had lost hope. They were ready to jump off the bridge and end their lives. Although a trained negotiator, Oakley also relied on his compassion, gentle voice, eye contact, and his innate ability to “listening to understand”. During his career, he encouraged more than 200 people not to jump, go over the bridge’s rail or come back to solid ground from where they had been standing precariously. These challenging, but rewarding efforts earned him the nickname, “Guardian of the Silverfall Span Bridge”. Retired, Oakley is now dedicating his life to promoting mental health awareness and suicide prevention across the globe.</p>
  </section>

  <svg class="pointer" width="76" height="14" viewBox="0 0 76 14" aria-hidden="true"><path d="M0 0 H76 L28 14 Z" fill="#fff"/></svg>

  <section class="agenda">
    <h3>Agenda</h3>
    <ul>
      <li><span class="time">8:30 am - 9:00 am</span>Registration, Breakefast and Opening</li>
      <li><span class="time">9:00 am - 9:45 am</span>Lorem Ipsum Sed ut perspiciatis unde omnis iste natus</li>
      <li><span class="time">10:00 am - 10:45 am</span>Registration, Breakefast and Opening</li>
      <li><span class="time">11:00 am - 12:00 m</span>Lorem Ipsum Sed ut perspiciatis unde omnis iste natus</li>
      <li><span class="time">1:00 pm - 1:45 am</span>sit voluptatem accusantium</li>
      <li><span class="time">2:00 pm - 2:45 am</span>sunt in culpa qui officia</li>
      <li><span class="time">3:00 pm - 4:00 pm</span>deserunt mollitia animi, id est laborum et dolorum fuga.</li>
    </ul>
  </section>

  <div class="badge">
    <div class="badge-ring">
      <div class="badge-mark">Lone Ridge Crisis Alliance</div>
    </div>
  </div>

  <div class="kicker">LONE RIDGE CRISIS ALLIANCE CONFERENCE</div>
  <div class="title-main">The Power</div>
  <div class="title-script"><small>of</small>Connection</div>
  <div class="title-year">2020</div>

  <section class="welcome">
    <h2>YOU ARE WELCOME</h2>
    <p>We are pleased to announce our 2020 Lone Ridge Crisis Alliance Association Conference, to be held April 23-25, 2020 in Amarillo, Texas. This two and a half day conference is expected to draw 200-250 attendees and will include sessions on specialized police responses to the mentally ill, developing successful collaborations between law enforcement and behavioral health providers, and developing public-private partnerships, and other relevant topics.</p>
  </section>

  <section class="registration">
    <h3>CONFERENCE REGISTRATION:</h3>
    <div class="price">$140 members until March 10 2020</div>
    <div class="price">$175 after March 10,&nbsp; 2020</div>
    <div class="price">$190 non-members</div>
    <p>Registering online will allow you to pay online after you complete the registration and print a payment receipt or print an invoice for payment by your department via department credit card or submission of a check on a later date.</p>
  </section>

  <div class="discounts">Early Bird and Member discounts</div>

  <div class="contact">
    <div class="q">Have a Conference Questions?</div>
    <div class="mail">
      <svg width="22" height="16" viewBox="0 0 22 16" aria-hidden="true"><rect x="1" y="1" width="20" height="14" rx="1.5" fill="none" stroke="#3a3a3a" stroke-width="2"/><path d="M1 2 L11 9 L21 2" fill="none" stroke="#3a3a3a" stroke-width="2"/></svg>
      E-mail: info@loneridgealliance.org
    </div>
  </div>

  <section class="sponsors">
    <div class="label">Our sponsors:</div>
    <div class="sponsor-row">
      <div class="sponsor-name">The Brookhaven</div>
      <div class="sponsor-name">Plainsview Visitors Bureau</div>
    </div>
  </section>

  <footer class="footer">
    <span>Discover Great sponsor opportunities at:</span>
    <strong>www.Loneridgealliance.org</strong>
  </footer>
</main>
</body>
</html>
```